Calm Summit website development

Need a website designed for a coaching business. Very high-end, luxury, professionalism, in the area of STRESS, see brief attached. I have a logo already
Updates

Slow in providing feedback

Target Market(s)

CEOs very successful men and wealthy females, high end luxury market

Industry/Entity Type

coaching

Number of Pages Required

1 page

Requirements
Must have
• Luxury look, professional, serious but warm, appealing to both sexes

```html
<!DOCTYPE html>
<html lang="en">
<head>
<meta charset="utf-8">
<title>Calm Summit — Stress Coaching</title>
<link rel="stylesheet" href="https://fonts.googleapis.com/css2?family=Montserrat:wght@500;600;700&family=Poppins:wght@400;500;600&display=swap">
<style>
:root{
  --ink:#1d1d1f;
  --text:#2b2b2b;
  --blue:#0b4e99;
  --yellow:#f6b21a;
  --white:#ffffff;
  --footer:#262324;
  --card-line:#e6e8ec;
  --icon-bg:#d6e2ec;
}
*{margin:0;padding:0;box-sizing:border-box}
html,body{width:1200px;height:4785px;overflow:hidden}
body{position:relative;background:var(--white);font-family:"Poppins",sans-serif;color:var(--text)}
.abs{position:absolute}
.heading{font-family:"Montserrat",sans-serif;font-weight:700;letter-spacing:6px;color:var(--ink);text-transform:uppercase}
.body-copy{font-size:16px;line-height:23px}
.body-copy p+p{margin-top:23px}

/* header */
.site-header{top:0;left:0;width:1200px;height:102px}
.main-nav{left:137px;top:49px;display:flex;gap:30px;font-size:12px;font-weight:500;letter-spacing:.5px}
.brand{left:0;width:1204px;top:36px;text-align:center;font-family:"Poppins",sans-serif;font-size:12px;font-weight:600;letter-spacing:4px;color:var(--ink)}
.brand .dot{display:block;width:26px;height:26px;border-radius:50%;background:var(--ink);margin:0 auto 6px}
.header-contact{left:768px;top:49px;display:flex;align-items:center;gap:6px;font-size:11.5px;font-weight:500}
.social{left:962px;top:51px;display:flex;gap:17px}
.social span{width:13px;height:13px;border-radius:50%;background:var(--ink)}

/* hero */
.hero{top:102px;left:0;width:1200px;height:522px;overflow:hidden}
.hero-women{left:0;top:0;width:700px;height:522px;background:linear-gradient(135deg,#6f5a44 0%,#b27650 45%,#d9b08a 75%,#8c6d52 100%);clip-path:polygon(0 0,700px 0,560px 522px,0 522px)}
.hero-men{left:560px;top:0;width:640px;height:522px;background:linear-gradient(160deg,#e7ddd0 0%,#bfb6ac 40%,#6e7684 70%,#3a4150 100%);clip-path:polygon(140px 0,640px 0,640px 522px,0 522px)}
.hero-btn{top:222px;height:48px;width:222px;border-radius:24px;font-family:"Montserrat",sans-serif;font-weight:700;font-size:12px;letter-spacing:.6px;color:var(--white);display:flex;align-items:center}
.btn-women{left:378px;background:var(--yellow);padding-left:30px}
.btn-men{left:602px;background:var(--blue);padding-left:60px;width:216px}
.hero-badge{left:564px;top:207px;width:78px;height:78px;border-radius:50%;background:var(--white)}

/* welcome */
.welcome-title{left:128px;top:763px;font-size:35px;line-height:44px}
.welcome-copy{left:128px;top:880px;width:460px}
.welcome-frame{left:676px;top:782px;width:416px;height:494px;background:var(--blue)}
.welcome-photo{left:622px;top:864px;width:513px;height:345px;background:linear-gradient(120deg,#8d7f6a 0%,#c3b59d 40%,#d8c9a5 60%,#6e6a5e 100%)}

.stress-hex{left:136px;top:1347px;width:397px;height:451px}
.stress-copy{left:596px;top:1398px;width:466px}

/* why me */
.why-band{top:1886px;left:0;width:1200px;height:533px;background:linear-gradient(100deg,#4a5552 0%,#6f7768 35%,#9c9f8d 60%,#5e6863 100%)}
.why-title{left:130px;top:2020px;font-size:33px;color:var(--white)}
.why-list{left:130px;top:2092px;width:480px;list-style:none;color:#eef0ea;font-size:16px;line-height:23px}
.why-list li{position:relative;padding-left:29px}
.why-list li+li{margin-top:23px}
.why-list svg{position:absolute;left:0;top:4px}

/* audience */
.audience-title{left:0;width:1200px;top:2510px;text-align:center;font-size:33px}
.audience-card{top:2610px;width:440px;height:403px;border:2px solid var(--card-line);border-radius:6px;box-shadow:0 2px 10px rgba(0,0,0,.06);text-align:center}
.card-women{left:141px}
.card-men{left:617px}
.audience-icon{width:108px;height:108px;border-radius:50%;background:var(--icon-bg);margin:36px auto 0}
.audience-card h3{font-family:"Poppins",sans-serif;font-weight:600;font-size:29px;color:var(--ink);margin-top:14px}
.audience-card p{font-size:14.5px;line-height:23px;width:360px;margin:12px auto 0}

/* athletes */
.athletes-band{top:3121px;left:0;width:1200px;height:501px;background:linear-gradient(180deg,#7d8089 0%,#a6a2a0 40%,#c4b8a8 65%,#6c6d72 100%)}
.athletes-title{left:297px;top:3244px;font-size:24px;letter-spacing:3px;color:var(--white);font-weight:600}
.athletes-list{left:303px;top:3288px;list-style:none;color:var(--white);font-family:"Montserrat",sans-serif;font-weight:600;font-size:17px}
.athletes-list li{height:36px;display:flex;align-items:center;gap:10px}
.athletes-hex{left:594px;top:3152px;width:394px;height:442px}

/* benefits */
.benefits-frame{left:45px;top:3812px;width:451px;height:541px;background:var(--blue)}
.benefits-photo{left:74px;top:3730px;width:480px;height:593px;background:linear-gradient(150deg,#3b2a22 0%,#9a6a4c 35%,#e5c29a 55%,#8a5a3c 80%,#2f2420 100%)}
.benefits-title{left:607px;top:3760px;font-size:35px}
.benefits-list{left:610px;top:3830px;width:490px;list-style:none;font-size:16px;line-height:23px}
.benefits-list li{position:relative;padding-left:24px}
.benefits-list li+li{margin-top:23px}
.benefits-list li::before{content:"";position:absolute;left:1px;top:6px;width:11px;height:11px;border-radius:50%;background:var(--ink)}

/* footer */
.site-footer{top:4443px;left:0;width:1200px;height:342px;background:var(--footer);color:var(--white)}
.footer-brand{left:0;width:1204px;top:4522px;text-align:center;font-size:12px;font-weight:600;letter-spacing:4px}
.footer-brand .dot{display:block;width:26px;height:26px;border-radius:50%;background:var(--white);margin:0 auto 6px}
.footer-contact{top:4597px;display:flex;align-items:center;gap:20px;font-size:15px;line-height:22px}
.footer-contact .ring{width:38px;height:38px;border:2px solid var(--white);border-radius:50%;display:flex;align-items:center;justify-content:center;flex:none}
.fc-phone{left:283px}
.fc-mail{left:508px}
.fc-address{left:776px}
.copyright{left:0;width:1200px;top:4693px;text-align:center;font-size:12.5px}
</style>
</head>
<body>

<header class="site-header abs">
  <nav class="main-nav abs"><span>HOME</span><span>ABOUT</span><span>SERVICES</span><span>CONTACT</span></nav>
  <div class="brand abs"><span class="dot"></span>CALM SUMMIT</div>
  <div class="header-contact abs">
    <svg width="13" height="13" viewBox="0 0 24 24"><path fill="#1d1d1f" d="M6.6 10.8a15.1 15.1 0 0 0 6.6 6.6l2.2-2.2a1 1 0 0 1 1-.25 11.4 11.4 0 0 0 3.6.57 1 1 0 0 1 1 1V20a1 1 0 0 1-1 1A17 17 0 0 1 3 4a1 1 0 0 1 1-1h3.5a1 1 0 0 1 1 1c0 1.25.2 2.45.57 3.57a1 1 0 0 1-.25 1z"/></svg>
    CALL US: 555 014 2290
  </div>
  <div class="social abs"><span></span><span></span><span></span><span></span></div>
</header>

<section class="hero abs">
  <div class="hero-women abs" role="img" aria-label="Smiling woman in an orange sweater holding a coffee cup"></div>
  <div class="hero-men abs" role="img" aria-label="Thoughtful businessman in a suit sitting at a desk"></div>
  <a class="hero-btn btn-women abs">WOMEN CLICK HERE</a>
  <a class="hero-btn btn-men abs">MEN CLICK HERE</a>
  <div class="hero-badge abs"></div>
</section>

<section class="welcome">
  <h1 class="heading welcome-title abs">Welcome<br>to Calm Summit</h1>
  <div class="body-copy welcome-copy abs">
    <p>Calm Summit came about due to my desire to help people lead a better and healthier life. Initially, I was involved in the fitness/body side of health. As years passed and my experience grew, I realized how important the mind was in total wellness, and that the mind is all powerful and controlling. Control the mind, control the body and achieve success. Stress can be the most debilating factor in our lives, it is the root cause of so many diseases and costs the US workplace an estimated 300 billion dollars due to loss of productivity.</p>
    <p>However stress is not all bad...we need stress to survive and peform at an optomial level. In order to do that, you need to recognize your stressors and then control them, and put it to good use when neccsary.</p>
  </div>
  <div class="welcome-frame abs"></div>
  <div class="welcome-photo abs" role="img" aria-label="Coaching session with a client on a sofa talking to a coach holding a clipboard"></div>
</section>

<section class="stress">
  <svg class="stress-hex abs" viewBox="0 0 397 451" role="img" aria-label="Woman writing notes at a desk, framed in a hexagon">
    <defs><linearGradient id="hexDesk" x1="0" y1="0" x2="1" y2="1"><stop offset="0" stop-color="#8fa3b3"/><stop offset=".5" stop-color="#dcdfe0"/><stop offset="1" stop-color="#9aa7b0"/></linearGradient></defs>
    <polygon points="198.5,0 397,112.75 397,338.25 198.5,451 0,338.25 0,112.75" fill="url(#hexDesk)"/>
  </svg>
  <div class="body-copy stress-copy abs">
    <p>Stress is not all bad, and since we are surrounded by engulfed by stress, or it isn't going anywhere soon, we need to deal with it, and even better, channel to be an advantage/tool to perform better.</p>
    <p>Recognize when we are feeling stress and what is causing it, understand it, and how we react to it is the first step. Then when we sense it's coming we can deal with it, resolve it, or use it to our advantage Effective stress control and problem solving skills may be the only thing that will keep your head above water in the next decade. It really is becoming quite serious and so should be taken very seriously. What is your plan for the next decade? Or, will you just let stress win?</p>
  </div>
</section>

<section class="why">
  <div class="why-band abs" role="img" aria-label="Man sitting on the ground, head in hand, under a cloud of tangled thoughts"></div>
  <h2 class="heading why-title abs">Why me?</h2>
  <ul class="why-list abs">
    <li><svg width="17" height="17" viewBox="0 0 20 20"><circle cx="10" cy="10" r="10" fill="#fff"/><path d="M5.5 10.3l3 3 6-6.3" fill="none" stroke="#5c665f" stroke-width="2.4"/></svg>Been there done that! Have been through a lot, started businesses, selling a business, law suits, marriage, divorce, second marriage, kids, school, sports, fights, robbed, gun in face, traveled the world, successful, two great kids (both Cadets at Ridgefield Academy Point...duty/honor/country)</li>
    <li><svg width="17" height="17" viewBox="0 0 20 20"><circle cx="10" cy="10" r="10" fill="#fff"/><path d="M5.5 10.3l3 3 6-6.3" fill="none" stroke="#5c665f" stroke-width="2.4"/></svg>Limited number of clients...different stage of life, empty nester, have a full career...won't be a number</li>
  </ul>
</section>

<section class="audience">
  <h2 class="heading audience-title abs">Target Audience</h2>
  <article class="audience-card card-women abs">
    <div class="audience-icon" role="img" aria-label="Woman avatar icon"></div>
    <h3>Women</h3>
    <p>General issues...I live near very wealthy neighborhoods with lots of "trophy wives" who are really quite lonely, as husbands work a great deal. They are also concerned with "fitting in" and acceptance...using wellness, yoga, aromatherapy,</p>
  </article>
  <article class="audience-card card-men abs">
    <div class="audience-icon" role="img" aria-label="Businessman avatar icon"></div>
    <h3>Men</h3>
    <p>The stress of success...they cannot share with anyone in fear of showing weakness...or a chink in the armor...not fully fulfilled, will provide and/or sign a confidentiality agreement. Fish where the big fish are: hedge fund companies: Greenwich is the epi center.</p>
  </article>
</section>

<section class="athletes">
  <div class="athletes-band abs" role="img" aria-label="Cloudy evening sky over a calm horizon"></div>
  <h2 class="heading athletes-title abs">Athletes:</h2>
  <ul class="athletes-list abs">
    <li><svg width="16" height="13" viewBox="0 0 16 13"><path d="M1 6.5l4.5 4.5L15 1" fill="none" stroke="#fff" stroke-width="2"/></svg>Performance stress</li>
    <li><svg width="16" height="13" viewBox="0 0 16 13"><path d="M1 6.5l4.5 4.5L15 1" fill="none" stroke="#fff" stroke-width="2"/></svg>Control</li>
    <li><svg width="16" height="13" viewBox="0 0 16 13"><path d="M1 6.5l4.5 4.5L15 1" fill="none" stroke="#fff" stroke-width="2"/></svg>Focus</li>
    <li><svg width="16" height="13" viewBox="0 0 16 13"><path d="M1 6.5l4.5 4.5L15 1" fill="none" stroke="#fff" stroke-width="2"/></svg>Visualization</li>
    <li><svg width="16" height="13" viewBox="0 0 16 13"><path d="M1 6.5l4.5 4.5L15 1" fill="none" stroke="#fff" stroke-width="2"/></svg>Anchoring</li>
    <li><svg width="16" height="13" viewBox="0 0 16 13"><path d="M1 6.5l4.5 4.5L15 1" fill="none" stroke="#fff" stroke-width="2"/></svg>Breathing</li>
  </ul>
  <svg class="athletes-hex abs" viewBox="0 0 394 442" role="img" aria-label="Two runners sprinting at sunset, framed in a hexagon">
    <defs><radialGradient id="hexRun" cx=".45" cy=".6" r=".7"><stop offset="0" stop-color="#fff3c9"/><stop offset=".35" stop-color="#f2b24d"/><stop offset="1" stop-color="#6b5a4e"/></radialGradient></defs>
    <polygon points="197,0 394,110.5 394,331.5 197,442 0,331.5 0,110.5" fill="url(#hexRun)"/>
  </svg>
</section>

<section class="benefits">
  <div class="benefits-frame abs"></div>
  <div class="benefits-photo abs" role="img" aria-label="Group of smiling women with heads together, seen from below"></div>
  <h2 class="heading benefits-title abs">Benefits</h2>
  <ul class="benefits-list abs">
    <li>Experience</li>
    <li>Sector expert Health/Wellness. Presented at numerous industry shows and quoted in national publications (not as a coach, I'm new, but in the health &amp; wellness space)</li>
    <li>Excellent listener...being in sales for many years, the secret is to really listen...and get to the end game, and make it feel as if it was their decision. Not sure how to word this as a benefit.</li>
    <li>Access/resources industry professionals, sport psychologist...just spent a few hours with the Mind performance coach for the Harbor City Pilots baseball team... I can get the best advice and latest techniques in mind/body training performance.</li>
    <li>Private, more than happy to sign confidentiality agreement. Especially for the business man.</li>
  </ul>
</section>

<footer class="site-footer abs"></footer>
<div class="footer-brand abs" style="color:var(--white)"><span class="dot"></span>CALM SUMMIT</div>
<div class="footer-contact fc-phone abs" style="color:var(--white)">
  <span class="ring"><svg width="16" height="16" viewBox="0 0 24 24"><path fill="#fff" d="M6.6 10.8a15.1 15.1 0 0 0 6.6 6.6l2.2-2.2a1 1 0 0 1 1-.25 11.4 11.4 0 0 0 3.6.57 1 1 0 0 1 1 1V20a1 1 0 0 1-1 1A17 17 0 0 1 3 4a1 1 0 0 1 1-1h3.5a1 1 0 0 1 1 1c0 1.25.2 2.45.57 3.57a1 1 0 0 1-.25 1z"/></svg></span>
  <div>Phone<br>+00 5550 1842</div>
</div>
<div class="footer-contact fc-mail abs" style="color:var(--white)">
  <span class="ring"><svg width="16" height="14" viewBox="0 0 16 12"><rect x="0.5" y="0.5" width="15" height="11" rx="1.5" fill="#fff"/><path d="M1 1l7 5.5L15 1" fill="none" stroke="#262324" stroke-width="1.4"/></svg></span>
  <div>Email<br>hello@calmsummit.example</div>
</div>
<div class="footer-contact fc-address abs" style="color:var(--white)">
  <span class="ring"><svg width="14" height="18" viewBox="0 0 14 18"><path d="M7 0a7 7 0 0 1 7 7c0 5-7 11-7 11S0 12 0 7a7 7 0 0 1 7-7z" fill="#fff"/><circle cx="7" cy="7" r="2.6" fill="#262324"/></svg></span>
  <div>Elm Row 12<br>2600 Westvale</div>
</div>
<div class="copyright abs" style="color:var(--white)">Copyright © 2022 All Right Reserved</div>

</body>
</html>
```